Etikett für Pure Ridge CBD Öl
Zielgruppe
Die Marke Pure Ridge verkauft CBD Hanf Öl.
Aufgabenstellung
Ich habe Ihnen ein Referenzprodukt bereitgestellt von meiner baldigen Marke Sky Drift, damit Sie sich etwas darunter vorstellen können.
-Was auf die Flasche drauf muss:
vorne:
das Logo Pure ridge
Hanf Öl
CBD aus Co2 Extraktion
Nahrungsergänzungsmittel
10 ml
Ich lasse mich mal überraschen, was Sie mir für Designs fertigstellen.
Bevorzugte Farben: weiß, Royal blue, schwarz, Gold, grün
Stellen Sie ein Design, dass zu dem Logo Pure Ridge passt.
Es soll sehr hochwertig aussehen. Auf den Gewinner warten regelmäßig weitere Produktdesigns und andere Designarbeiten von Pure Ridge aus Deutschland und Sky Drift aus Spanien.
hinten klein:
Empfohlene Tagesdosis: 2x 5-10 Tropfen
Die maximale Tagesdosierung von 20 Tropfen darf nicht überschritten werden
Nahrungsergänzungsmittel dienen nicht als Ersatz für eine abwechslungsreiche und ausgewogene Ernährung.
Lagern Sie das Produkt kühl, dunkel und außerhalb der Reichweite von Kindern.
Zutaten: Hanfsamenöl: 2295mg(77%), Hanfextrakt: 2295 mg(23%)
CBD 500mg, entspricht 37mg/ empfohlener Tagesdosis
Mindestens haltbar bis 01.03.2019
Chargernummer DE/417/6081
Anbaugebiet: EU
Vertrieb: TKB UG
Lindauer Weg 14
71388 Leonberg

```html
<!DOCTYPE html>
<html lang="de">
<head>
<meta charset="utf-8">
<title>Pure Ridge – Hanf Öl Etikett</title>
<link rel="stylesheet" href="https://fonts.googleapis.com/css2?family=Montserrat:wght@400;500;600;700&family=Yellowtail&display=swap">
<style>
  :root {
    --backdrop: #efefef;
    --royal: #1f3d94;
    --gold-light: #f3d36a;
    --gold: #d9a92c;
    --gold-dark: #a87a12;
    --white: #ffffff;
  }
  * { box-sizing: border-box; margin: 0; padding: 0; }
  html, body { width: 1200px; height: 975px; overflow: hidden; }
  body {
    background: var(--backdrop);
    font-family: "Montserrat", Arial, sans-serif;
    display: flex;
    align-items: center;
    justify-content: center;
    gap: 60px;
  }
  .label {
    position: relative;
    width: 500px;
    height: 600px;
    background: var(--royal);
    overflow: hidden;
    box-shadow: 0 8px 30px rgba(0,0,0,0.12);
  }
  .label__top-strip {
    position: absolute; top: 0; left: 0; right: 0;
    height: 24px; background: var(--white);
  }
  .label__gold-band {
    position: absolute; left: 0; right: 0; bottom: 0;
    height: 150px;
    background: linear-gradient(180deg, var(--gold-light) 0%, var(--gold) 45%, var(--gold-dark) 100%);
    color: var(--white);
    padding: 26px 34px;
    z-index: 2;
  }
  .leaf-decoration {
    position: absolute;
    width: 170px; height: 190px;
    background: radial-gradient(ellipse at center, rgba(243,211,106,0.55) 0%, rgba(217,169,44,0.25) 55%, rgba(31,61,148,0) 75%);
  }

  /* Front */
  .brand {
    position: absolute; top: 46px; left: 60px;
    width: 200px;
    display: flex; flex-direction: column; align-items: center; gap: 12px;
  }
  .brand__circle {
    width: 96px; height: 96px; border-radius: 50%;
    background: var(--white);
    border: 5px solid var(--gold);
  }
  .brand__name {
    font-weight: 600; font-size: 20px; color: var(--white);
    letter-spacing: 2px; text-transform: uppercase;
  }
  .product-title {
    position: absolute; right: 18px; top: 36px; bottom: 162px;
    width: 120px;
    display: flex; align-items: center; justify-content: center;
    writing-mode: vertical-rl;
    transform: rotate(180deg);
    font-family: "Yellowtail", cursive;
    font-size: 104px; line-height: 1;
    color: var(--gold);
    white-space: nowrap;
  }
  .front .leaf-decoration { left: -40px; bottom: 140px; }
  .band-row {
    display: flex; justify-content: space-between; align-items: baseline;
    font-weight: 600; font-size: 20px;
  }
  .band-divider {
    height: 2px; background: var(--white); opacity: 0.85;
    margin: 18px 0 16px;
  }
  .band-row sub { font-size: 12px; }

  /* Back */
  .info {
    position: absolute; top: 58px; left: 34px; right: 50px;
    color: var(--white);
  }
  .info p { font-size: 15px; font-weight: 500; line-height: 1.4; margin-bottom: 16px; }
  .info .info__small { font-size: 12px; font-weight: 400; margin-bottom: 12px; }
  .back .leaf-decoration { right: -40px; bottom: 140px; }
  .back .label__gold-band {
    display: flex; justify-content: space-between;
    font-size: 15px; font-weight: 500; line-height: 1.5;
  }
  .origin { display: flex; flex-direction: column; justify-content: space-between; }
</style>
</head>
<body>

  <section class="label front">
    <div class="label__top-strip"></div>
    <div class="brand">
      <span class="brand__circle"></span>
      <span class="brand__name">Pure Ridge</span>
    </div>
    <div class="product-title">hanf öl</div>
    <div class="leaf-decoration" role="img" aria-label="Goldene Hanfblatt-Verzierung"></div>
    <div class="label__gold-band">
      <div class="band-row"><span>CBD aus CO<sub>2</sub> Extraktion</span><span>| &nbsp;5% CBD</span></div>
      <div class="band-divider"></div>
      <div class="band-row"><span>Nahrungsergänzungsmittel</span><span>10ml</span></div>
    </div>
  </section>

  <section class="label back">
    <div class="label__top-strip"></div>
    <div class="info">
      <p>Empfohlene Tagesdosis: 2x 5-10 Tropfen. Die maximale Tagesdosierung von 20 Tropfen darf nicht überschritten werden.</p>
      <p>Nahrungsergänzungsmittel dienen nicht als Ersatz für eine abwechslungsreiche und ausgewogene Ernährung.</p>
      <p>Lagern Sie das Produkt kühl, dunkel und außerhalb der Reichweite von Kindern.</p>
      <p>Zutaten: Hanfsamenöl: 2295mg (77%),<br>Hanfextrakt: 2295 mg (23%)</p>
      <p class="info__small">CBD 500mg, entspricht 37mg/<br>empfohlener Tagesdosis</p>
      <p class="info__small">Mindestens haltbar bis 01.03.2019</p>
    </div>
    <div class="leaf-decoration" role="img" aria-label="Goldene Hanfblatt-Verzierung"></div>
    <div class="label__gold-band">
      <div class="origin">
        <span>Anbaugebiet: EU</span>
        <span>L DE/417/6081</span>
      </div>
      <div class="distributor">
        Vertrieb: TKB UG<br>Lindauer Weg 14<br>71388 Leonberg
      </div>
    </div>
  </section>

</body>
</html>
```